Red heron

Retail sales of clothing related to outdoor sports, exercise, activities and socialization
Updates

please use more clothing accessories
golf beach sports running yoga pilates gym etc rather than equipment for now

please use logo designed

hello

can I get a link / page to
RED HERON MENTAL HEALTH GROUP CIC
promoting outdoor activities, exercis, outdoors and socialization to help with mental health issues
Courage strength and loyalty

use the social media image 2 wolves howling to the moon

Please

This is a non profit charity
proceeds from red heron LLC sales will be donated to this non profit company to help those in UK with mental health issues

Target Market(s)

All

Industry/Entity Type

Retail e-commerce

Coding

Coded - Design and coding required

Number of Pages Required

5+ page

Font styles to use
Other font styles liked:
• To fit with red heron logo design

Colors
0054AA
0677BA
7BADD7
CADEEF
E8F1F8

Requirements
Must have
• Ability to accept payments, link to a not for profit business to be supplied for donations of proceeds of sale, ability to link to activities
Nice to have
• Ai associated customers service, email, blog, WhatsApp, links to social media

```html
<!DOCTYPE html>
<html lang="en">
<head>
<meta charset="utf-8">
<title>Red Heron – Outdoor Retail</title>
<link rel="stylesheet" href="https://fonts.googleapis.com/css2?family=Cinzel:wght@400;500&family=Poppins:wght@400;500;600;700&display=swap">
<style>
:root{
  --blue:#0b57d8;
  --navy:#1a2a8c;
  --navy-dark:#102486;
  --ink:#333844;
  --grey-bg:#f3f3f4;
  --white:#ffffff;
}
*{margin:0;padding:0;box-sizing:border-box}
html,body{width:1200px;height:4823px;overflow:hidden;background:var(--white)}
body{font-family:"Poppins",sans-serif;color:var(--ink)}
.page{position:relative;width:1200px;height:4823px;overflow:hidden}
.abs{position:absolute}
.serif{font-family:"Cinzel",serif}
.btn{position:absolute;display:flex;align-items:center;justify-content:center;border-radius:30px;font-weight:600;font-size:15px;color:var(--white);text-transform:uppercase;letter-spacing:.2px}

/* header */
.site-header{position:absolute;left:0;top:0;width:1200px;height:97px;background:var(--white)}
.brand{position:absolute;display:flex;align-items:center;gap:8px;font-family:"Cinzel",serif;color:var(--blue);line-height:.9}
.brand-mark{border:2.5px solid var(--navy);border-radius:50%}
.brand-name{font-size:26px;font-weight:500}
.nav a{position:absolute;top:40px;font-size:13px;font-weight:500;color:#1e2230;text-decoration:none}
.nav a.active{color:var(--blue)}
.cart{position:absolute;left:920px;top:34px}
.btn-donate{left:962px;top:22px;width:186px;height:53px;background:var(--blue);font-size:14px}

/* hero */
.hero-photo{position:absolute;left:0;top:97px;width:1200px;height:568px;
  background:
    radial-gradient(ellipse 260px 300px at 420px 300px,rgba(40,50,120,.55) 0%,rgba(40,50,120,0) 70%),
    linear-gradient(62deg,#ffffff 0%,#eef2f8 24%,#d3dff0 33%,#7ea4e6 42%,#3f73dc 54%,#1450cc 72%,#0a41b8 100%)}
.hero-title{left:640px;top:230px;font-size:76px;color:var(--white);font-weight:400;letter-spacing:1px}
.hero-sub{left:641px;top:334px;width:480px;font-size:30px;line-height:41px;color:var(--white)}
.btn-hero{left:642px;top:436px;width:152px;height:56px;background:var(--navy-dark)}

/* about */
.about{position:absolute;left:0;top:665px;width:1200px;height:608px;background:var(--grey-bg)}
.about-mark{left:122px;top:131px;width:286px;height:368px;display:flex;align-items:center;justify-content:center}
.about-mark .circle{width:270px;height:270px;border:4px solid var(--blue);border-radius:50%;display:flex;align-items:center;justify-content:center;font-family:"Cinzel",serif;font-size:32px;color:var(--blue)}
.about h2{left:492px;top:130px;font-size:44px;font-weight:400;color:var(--navy)}
.about h2 span{color:var(--blue)}
.about p{left:492px;top:208px;width:572px;font-size:14.6px;line-height:23.2px;color:#3a3f4a}
.btn-about{left:492px;top:453px;width:152px;height:56px;background:var(--blue)}

/* activities */
.activities h2{left:0;top:1378px;width:1200px;text-align:center;font-size:40px;font-weight:600;color:var(--navy)}
.activities .lead{left:180px;top:1450px;width:840px;text-align:center;font-size:14.5px;line-height:23px;color:#2a2f3a}
.tile{position:absolute;width:287px;height:249px;overflow:hidden}
.tile-photo{position:absolute;inset:0}
.tile-photo::after{content:"";position:absolute;inset:0;background:rgba(0,0,0,.12)}
.tile-label{position:absolute;inset:0;display:flex;align-items:center;justify-content:center;font-weight:700;font-size:18px;color:var(--white);text-transform:uppercase;text-shadow:0 1px 4px rgba(0,0,0,.55)}
.divider{position:absolute;left:0;top:2156px;width:1200px;height:3px;background:var(--navy)}
.divider-accent{position:absolute;left:865px;top:2153px;width:335px;height:7px;background:var(--blue)}

/* sales */
.sales-bg{position:absolute;left:0;top:2211px;width:1200px;height:685px;
  background:linear-gradient(180deg,#1657d9 0%,#1d5fdf 30%,#3a74e0 58%,#245ed6 75%,#1a52c8 100%)}
.sales h2{left:0;top:2268px;width:1200px;text-align:center;font-size:44px;font-weight:400;color:var(--white)}
.card{position:absolute;background:var(--white);text-align:center}
.card-photo{position:absolute;left:40px;top:30px;right:40px;height:180px;border-radius:50%}
.card h3{position:absolute;left:0;right:0;font-size:22px;font-weight:600;color:var(--navy)}
.card p{position:absolute;left:30px;right:30px;font-size:13.6px;line-height:20px;color:#7a7f8a}
.arrow{position:absolute;width:54px;height:54px;border:2.5px solid var(--white);border-radius:50%;display:flex;align-items:center;justify-content:center}

/* blog */
.blog h2{left:0;top:2985px;width:1200px;text-align:center;font-size:44px;font-weight:400;color:var(--navy)}
.post{position:absolute;top:3095px;width:223px}
.post-photo{width:223px;height:297px}
.post h3{margin-top:26px;font-size:21px;line-height:27px;font-weight:600;color:var(--blue)}
.post p{margin-top:16px;font-size:13.8px;line-height:20px;color:#5a5f6a}
.btn-view{left:524px;top:3650px;width:152px;height:57px;background:var(--blue)}
.rule{position:absolute;left:127px;top:3769px;width:946px;height:2px;background:var(--blue)}

/* newsletter */
.newsletter{position:absolute;left:127px;top:3843px;width:946px;height:182px;border-radius:91px;background:var(--blue)}
.newsletter h2{left:62px;top:72px;font-size:28px;font-weight:700;color:var(--white)}
.newsletter .field{left:405px;top:70px;width:310px;height:32px;border-bottom:1.5px solid var(--white);font-size:13px;color:var(--white)}
.btn-news{left:747px;top:66px;width:143px;height:52px;background:var(--navy-dark);font-size:16px}

/* footer */
.footer-photo{position:absolute;left:0;top:4025px;width:1200px;height:798px;
  background:
    radial-gradient(ellipse 380px 260px at 420px 720px,rgba(30,70,140,.45) 0%,rgba(30,70,140,0) 70%),
    linear-gradient(180deg,#ffffff 0%,#ffffff 44%,#eef2f7 56%,#d6e0eb 72%,#b9c9dc 88%,#9fb4cf 100%)}
.footer-about{left:127px;top:4188px;width:220px;font-size:15px;line-height:25.5px;color:#222}
.foot-col h4{position:absolute;font-size:20px;font-weight:600;color:#1e2230}
.foot-col ul{position:absolute;list-style:none}
.foot-col li{font-size:14.6px;line-height:32px;color:#222}
.foot-col li.active{color:var(--blue)}
.foot-email{left:771px;top:4145px;width:302px;height:50px;border:1px solid #dde1e7;border-radius:25px;background:var(--white);padding:15px 20px;font-size:12px;font-weight:600;color:#222}
.btn-foot{left:771px;top:4208px;width:302px;height:51px;background:var(--blue);font-size:16px}
.social{position:absolute;top:4281px;width:34px;height:34px;border-radius:50%}
.pay{position:absolute;top:4409px;width:64px;height:44px;border-radius:5px;background:var(--white);box-shadow:0 1px 4px rgba(0,0,0,.18);display:flex;align-items:center;justify-content:center;font-size:12px;font-weight:600;color:var(--navy)}
</style>
</head>
<body>
<div class="page">

  <header class="site-header">
    <div class="brand" style="left:54px;top:22px">
      <span class="brand-mark" style="width:44px;height:44px"></span>
      <span class="brand-name">RED<br>HERON</span>
    </div>
    <nav class="nav">
      <a class="active" style="left:257px">HOME</a>
      <a style="left:330px">ABOUT</a>
      <a style="left:412px">PRODUCTS</a>
      <a style="left:517px">RETAIL BUYERS</a>
      <a style="left:648px">BLOG</a>
      <a style="left:716px">ACTIVITIES</a>
      <a style="left:820px">CONTACT</a>
    </nav>
    <svg class="cart" width="22" height="26" viewBox="0 0 22 26" aria-label="Cart">
      <rect x="2" y="7" width="18" height="17" rx="2" fill="none" stroke="#0b57d8" stroke-width="2"/>
      <path d="M7 10V6a4 4 0 0 1 8 0v4" fill="none" stroke="#0b57d8" stroke-width="2"/>
    </svg>
    <div class="btn btn-donate">Donated per sale</div>
  </header>

  <section class="hero">
    <div class="hero-photo" role="img" aria-label="Skier carving down a snowy slope under a deep blue sky"></div>
    <h1 class="abs serif hero-title">RED HERON</h1>
    <p class="abs hero-sub">Retail sales of outdoor sports and socialization.</p>
    <div class="btn btn-hero">Shop now</div>
  </section>

  <section class="about">
    <div class="abs about-mark"><div class="circle">RED HERON</div></div>
    <h2 class="abs serif">ABOUT <span>RED HERON</span></h2>
    <p class="abs">Sed ut perspiciatis unde omnis iste natus error sit voluptatem accusa ntium doloremque laudantiumotamrem aperiam, eaque ipsa quae ab illo inventore veritatis et quasi architecto beatae vitae dicta sunt explicabo. Nemo enim ipsam voluptatem quia voluptas sit aspernatur aut odit autfu gitsed quia consequuntur magni dolores eos qui ratione voluptatem sequi nesciunt. Neque porro quisquam eui dolorem ipsum quia dolor sit amet, consectetur, adipisci velit, sed quia non numquamem vel eum iure reprhe nderit qui in ea voluptate velit esse quam nihil molestiae consequatuvel illum qui dolorem eum fugiat quo volu.</p>
    <div class="btn btn-about">Shop now</div>
  </section>

  <section class="activities">
    <h2 class="abs">Activities-Focused with Retail Buyers</h2>
    <p class="abs lead">Lorem ipsum dolor sit amet, consectetur adipiscing elit, sed do eiusmod tempor incididunt ut labore et dolore magna aliis ipsum suspendisse ultrices gravid commodo viverra maecenas accumsan lacilisis.</p>

    <div class="tile" style="left:127px;top:1526px">
      <div class="tile-photo" role="img" aria-label="Hikers with backpacks in snowy mountains" style="background:linear-gradient(180deg,#1f4fb0 0%,#5d86cc 30%,#dfe6ee 48%,#b5443a 66%,#6d2a2a 82%,#3b3030 100%)"></div>
      <span class="tile-label">Camp+Hike</span>
    </div>
    <div class="tile" style="left:457px;top:1526px">
      <div class="tile-photo" role="img" aria-label="Cyclists riding along a mountain road" style="background:linear-gradient(180deg,#a29378 0%,#7a6a55 35%,#4a4640 58%,#b6b3ab 78%,#8d8a83 100%)"></div>
      <span class="tile-label">Run + Cycle</span>
    </div>
    <div class="tile" style="left:786px;top:1526px">
      <div class="tile-photo" role="img" aria-label="Kayaker paddling a yellow kayak on tropical water" style="background:linear-gradient(180deg,#cfd8d6 0%,#6f9a7a 28%,#2f6a4c 48%,#4e8f8a 62%,#e3c53a 80%,#c39a2a 100%)"></div>
      <span class="tile-label">Water Sports</span>
    </div>
    <div class="tile" style="left:127px;top:1806px">
      <div class="tile-photo" role="img" aria-label="Climbers helping each other up a rocky summit" style="background:linear-gradient(120deg,#5a4538 0%,#7a5a48 28%,#c9d2da 45%,#8fa2b4 65%,#3e4a58 100%)"></div>
      <span class="tile-label">Climb</span>
    </div>
    <div class="tile" style="left:457px;top:1806px">
      <div class="tile-photo" role="img" aria-label="Friends relaxing together on a picnic blanket" style="background:linear-gradient(180deg,#3f6a2a 0%,#6d8a3a 30%,#8a5a3a 55%,#d8b84a 78%,#a87a2a 100%)"></div>
      <span class="tile-label">Socialization</span>
    </div>
    <div class="tile" style="left:786px;top:1806px">
      <div class="tile-photo" role="img" aria-label="Store assistant with a tablet beside clothing racks" style="background:linear-gradient(90deg,#3d3e44 0%,#6e6f75 35%,#c9c6c0 60%,#eeeae4 100%)"></div>
      <span class="tile-label">Retail Services</span>
    </div>
  </section>

  <div class="divider"></div>
  <div class="divider-accent"></div>

  <section class="sales">
    <div class="sales-bg" role="img" aria-label="Snow-covered forest tinted in blue"></div>
    <h2 class="abs serif">LATEST SALES OF GOODS</h2>

    <div class="arrow" style="left:35px;top:2538px">
      <svg width="16" height="16" viewBox="0 0 16 16"><path d="M10 2L4 8l6 6" fill="none" stroke="#fff" stroke-width="2"/></svg>
    </div>
    <div class="arrow" style="left:1098px;top:2538px">
      <svg width="16" height="16" viewBox="0 0 16 16"><path d="M6 2l6 6-6 6" fill="none" stroke="#fff" stroke-width="2"/></svg>
    </div>

    <div class="card" style="left:127px;top:2379px;width:294px;height:397px">
      <div class="card-photo" role="img" aria-label="Colourful skateboard" style="background:linear-gradient(135deg,#f3a0c0 0%,#f7d25a 35%,#6fb8e8 65%,#8a7ad8 100%)"></div>
      <h3 style="top:262px">Product Name</h3>
      <p style="top:298px">Lorem ipsum dolor sit amet, consectetur adipiscing elit, sed do eiusmod tempor incid</p>
    </div>
    <div class="card" style="left:453px;top:2379px;width:294px;height:397px">
      <div class="card-photo" role="img" aria-label="Electric kick scooter" style="background:linear-gradient(135deg,#d9dce1 0%,#8e939b 45%,#2c2f35 100%)"></div>
      <h3 style="top:262px">Product Name</h3>
      <p style="top:298px">Lorem ipsum dolor sit amet, consectetur adipiscing elit, sed do eiusmod tempor incid</p>
    </div>
    <div class="card" style="left:780px;top:2368px;width:294px;height:436px;border-radius:147px">
      <div class="card-photo" role="img" aria-label="Red hiking backpack with boots and sleeping mat" style="top:40px;left:50px;right:50px;background:linear-gradient(160deg,#e04848 0%,#c22e34 40%,#6f7a8c 75%,#3d4350 100%)"></div>
      <h3 style="top:273px">Product Name</h3>
      <p style="top:309px">Lorem ipsum dolor sit amet, consectetur adipiscing elit, sed do eiusmod tempor incid</p>
    </div>
  </section>

  <section class="blog">
    <h2 class="abs serif">LATEST BLOG</h2>

    <article class="post" style="left:127px">
      <div class="post-photo" role="img" aria-label="Football on grass at sunset" style="background:linear-gradient(180deg,#f2c877 0%,#e0a24a 35%,#8c6a2e 62%,#4a5a22 82%,#2a3014 100%)"></div>
      <h3>Lorem ipsum dolor sit ame consec.</h3>
      <p>Lorem ipsum dolor sit amet, consectetur adipiscing elit, sed do eiusmod tempor inc ididunt ut labore et dolore magna aliqua.</p>
    </article>
    <article class="post" style="left:369px">
      <div class="post-photo" role="img" aria-label="Pair of skis planted in snow against mountains" style="border-radius:50%;background:linear-gradient(180deg,#1f4fae 0%,#3f6fc4 40%,#8aa4cf 62%,#e8eef5 82%,#ffffff 100%)"></div>
      <h3>Lorem ipsum dolor sit ame consec.</h3>
      <p>Lorem ipsum dolor sit amet, consectetur adipiscing elit, sed do eiusmod tempor inc ididunt ut labore et dolore magna aliqua.</p>
    </article>
    <article class="post" style="left:608px">
      <div class="post-photo" role="img" aria-label="Two climbers high-fiving in the mountains" style="background:linear-gradient(180deg,#c7d0d8 0%,#9aa8b4 28%,#2f9aa6 50%,#b2364a 66%,#4a4a52 100%)"></div>
      <h3>Lorem ipsum dolor sit ame consec.</h3>
      <p>Lorem ipsum dolor sit amet, consectetur adipiscing elit, sed do eiusmod tempor inc ididunt ut labore et dolore magna aliqua.</p>
    </article>
    <article class="post" style="left:850px">
      <div class="post-photo" role="img" aria-label="Woman paddling a yellow kayak" style="background:linear-gradient(180deg,#dfe6ea 0%,#8fb0bf 30%,#3c7690 55%,#f0c93a 75%,#d8a82a 100%)"></div>
      <h3>Lorem ipsum dolor sit ame consec.</h3>
      <p>Lorem ipsum dolor sit amet, consectetur adipiscing elit, sed do eiusmod tempor inc ididunt ut labore et dolore magna aliqua.</p>
    </article>

    <div class="btn btn-view">View all</div>
  </section>

  <div class="rule"></div>

  <section class="newsletter">
    <h2 class="abs">NEWSLETTER SIGNUP</h2>
    <div class="abs field">Email:</div>
    <div class="btn btn-news">Sign up</div>
  </section>

  <footer>
    <div class="footer-photo" role="img" aria-label="Group of skiers descending a snowy slope"></div>
    <div class="brand" style="left:127px;top:4094px">
      <span class="brand-mark" style="width:50px;height:50px"></span>
      <span class="brand-name" style="font-size:28px">RED<br>HERON</span>
    </div>
    <p class="abs footer-about">Lorem ipsum dolor sit am et, consectetur adipiscing elit, sed do eiusmod tem por incididunt ut labore et dolore magna aliqua.</p>

    <div class="foot-col">
      <h4 style="left:371px;top:4090px">Customers Service</h4>
      <ul style="left:375px;top:4133px">
        <li>Support</li><li>Track My Order</li><li>Return Policy</li><li>Flagship Store</li><li>Store Locator</li><li>Wholesale</li><li>Corporate Gifting</li>
      </ul>
    </div>
    <div class="foot-col">
      <h4 style="left:636px;top:4090px">Links</h4>
      <ul style="left:639px;top:4133px">
        <li class="active">Home</li><li>About</li><li>Products</li><li>Retail Buyers</li><li>Blog</li><li>Activities</li><li>Contact</li>
      </ul>
    </div>
    <div class="foot-col">
      <h4 style="left:771px;top:4090px">Newsletter</h4>
    </div>
    <div class="abs foot-email">Email:</div>
    <div class="btn btn-foot">Sign up</div>

    <span class="social" style="left:782px;background:#1f5fd0" aria-label="Social link"></span>
    <span class="social" style="left:820px;background:#8c8f96" aria-label="Social link"></span>
    <span class="social" style="left:857px;background:#8c8f96" aria-label="Social link"></span>
    <span class="social" style="left:896px;background:#8c8f96" aria-label="Social link"></span>
    <span class="social" style="left:934px;background:#8c8f96" aria-label="Social link"></span>

    <span class="pay" style="left:382px">Roamly</span>
    <span class="pay" style="left:455px">Circa</span>
    <span class="pay" style="left:528px">Amplo</span>
    <span class="pay" style="left:601px">Strivo</span>
    <span class="pay" style="left:674px">Vela</span>
    <span class="pay" style="left:747px">Paywell</span>
  </footer>

</div>
</body>
</html>
```